Budget planning & tracking app

I want to make personal budget planning and tracking easier and more enjoyable for people from all walks of life. I will aim to assist students, graduates, young professionals and anyone else interested, to get a grip on their personal finances early-on in life, allowing them to build their wealth plan to retirement, and also giving them an easy way to track their financial performance. I want to develop an intuative app that will make capturing daily transaction details a seamless and easy process.

Target Market(s)

This app must appeal to anyone in need of an easy and intuative solution to track their daily finances and to understand what their current lifestyle will mean for their wealth building..

Industry/Entity Type

Personal finance

Font styles to use
Sans Serif

Requirements
Must have
• Super easy and intuative interface, easy capturing of actual expenses, easy setup of planned income and expenses, visual representation of wealth building over time.
Nice to have
• Would be nice if there's.some way to present the solution in a gaming interface, so capturing daily expenses feels less like a chore and more like a game.
Should not have
• Should not look like a spreadsheet.

```html
<!DOCTYPE html>
<html lang="en">
<head>
<meta charset="utf-8">
<title>Budget App – Screens</title>
<link href="https://fonts.googleapis.com/css2?family=Poppins:wght@400;500;600;700;800&display=swap" rel="stylesheet">
<style>
:root{
  --blue:#2f46f5;
  --blue-deep:#1b2466;
  --screen:#161b24;
  --card:#20262f;
  --card-2:#1c2129;
  --line:#2d3441;
  --text:#ffffff;
  --muted:#8b93a3;
  --accent:#2a45ff;
  --accent-soft:#5b73ff;
  --red:#e5484d;
  --orange:#e2913a;
  --green:#35b27a;
}
*{box-sizing:border-box;margin:0;padding:0}
html,body{width:1200px;height:2428px;overflow:hidden;background:var(--blue)}
body{font-family:"Poppins",Arial,sans-serif;color:var(--text)}
.stage{position:relative;width:1273px;height:2576px;transform:scale(0.94266);transform-origin:0 0;background:var(--blue)}
svg{display:block}

/* hero */
.hero{position:absolute;left:0;top:0;width:1273px;height:800px;overflow:hidden;background:linear-gradient(180deg,var(--blue) 0%,var(--blue) 40%,#26349e 70%,var(--blue-deep) 100%)}
.hero-brand{position:absolute;left:18px;top:116px;display:flex;align-items:center;gap:12px;font-size:36px;font-weight:700;letter-spacing:-.5px}
.hero-brand i{width:26px;height:26px;background:#fff;border-radius:4px}
.hero-word{position:absolute;left:0;right:0;top:575px;text-align:center;font-size:200px;font-weight:800;color:rgba(255,255,255,.07);letter-spacing:-4px;white-space:nowrap}
.hero .screen{border-radius:16px;box-shadow:0 20px 50px rgba(0,0,0,.35)}

/* screen base */
.screen{position:absolute;width:163px;background:var(--screen);overflow:hidden;color:var(--text)}
.status{display:flex;justify-content:space-between;align-items:center;padding:6px 12px 0;font-size:6px;font-weight:500}
.status svg{width:22px;height:6px}
.homebar{position:absolute;bottom:4px;left:50%;width:56px;height:2px;margin-left:-28px;background:#fff;border-radius:2px}
.bar{position:relative;height:22px;margin-top:6px;display:flex;align-items:center;justify-content:center;border-bottom:1px solid var(--line);font-size:7.5px;font-weight:600}
.bar.left{justify-content:flex-start;padding-left:8px}
.back{position:absolute;left:8px;width:10px;height:10px;border:1px solid #59606e;border-radius:50%;display:flex;align-items:center;justify-content:center;color:#c8cdd6}
.back svg{width:6px;height:6px}
.avatar{position:absolute;right:8px;width:14px;height:14px;border-radius:50%;background:linear-gradient(135deg,#c9b49c,#6f5b4b)}

.brand{display:flex;align-items:center;justify-content:center;gap:5px;font-weight:700;font-size:10px}
.brand i{width:9px;height:9px;background:var(--accent);border-radius:2px}
.brand-stack{display:flex;flex-direction:column;align-items:center;gap:6px;font-weight:700;font-size:10px;margin-top:30px}
.brand-stack i{width:22px;height:22px;background:var(--accent);border-radius:4px}

.lbl{font-size:5.5px;color:var(--muted);margin:0 10px 4px}
.field{display:flex;align-items:center;gap:5px;height:18px;padding:0 6px;border:1px solid var(--line);background:#1d232c;border-radius:4px;font-size:6px;color:var(--muted);margin:0 10px 10px}
.field.on{border-color:var(--accent);color:#fff}
.field.err{border-color:var(--red);color:#fff}
.field svg{width:7px;height:7px;flex:none}
.field .end{margin-left:auto;color:var(--muted)}
.btn{margin:0 10px;height:18px;border-radius:4px;background:var(--accent);font-size:6px;font-weight:600;display:flex;align-items:center;justify-content:center;text-transform:uppercase;letter-spacing:.2px}
.btn.pin{position:absolute;left:0;right:0;bottom:32px}
.btn.ghost{background:transparent;border:1px solid var(--line);gap:8px;justify-content:flex-start;padding-left:8px}
.btn.ghost b{width:7px;height:7px;border-radius:50%;background:#fff}
.center-note{text-align:center;font-size:5.5px;color:var(--muted);margin:10px 0}
.center-note a{color:var(--accent-soft);text-decoration:none}

/* onboarding */
.art{margin:20px auto 0;width:96px;height:96px;border-radius:50%;background:radial-gradient(circle at 40% 40%,#3d58ff,#1f33c4 70%)}
.ob-title{text-align:center;font-size:7.5px;font-weight:600;margin-top:30px}
.ob-text{text-align:center;font-size:5.5px;color:var(--muted);line-height:1.5;margin:4px 18px 0}
.dots{display:flex;justify-content:center;gap:3px;margin-top:8px}
.dots i{width:6px;height:1.5px;background:#3a4150}
.dots i.on{background:var(--accent)}

/* keyboard */
.kbd{position:absolute;left:0;right:0;bottom:0;background:#1d222b;padding:4px 2px 20px}
.krow{display:flex;gap:2px;justify-content:center;margin-bottom:4px}
.krow span{width:13px;height:17px;background:#2c323d;border-radius:2px;font-size:7.5px;display:flex;align-items:center;justify-content:center}
.krow span.w{width:20px;font-size:5px;background:#3a404b}
.krow span.sp{width:70px;font-size:5.5px}
.krow span.go{width:32px;font-size:5px;background:#3a404b}
.kfoot{display:flex;justify-content:space-between;padding:0 12px;margin-top:4px;color:#c8cdd6}
.kfoot svg{width:9px;height:9px}

/* cards & lists */
.card{background:var(--card);border-radius:6px;margin:8px;padding:6px}
.sec{display:flex;justify-content:space-between;align-items:center;font-size:6.5px;font-weight:600;margin:10px 10px 4px}
.more{width:14px;height:10px;border:1px solid #59606e;border-radius:3px;display:flex;align-items:center;justify-content:center}
.more svg{width:8px;height:3px}
.entries{padding:0 10px}
.entry{display:flex;align-items:center;gap:5px;padding:5.5px 0}
.ico{width:14px;height:14px;border-radius:3px;background:var(--red);flex:none;position:relative}
.ico:after{content:"";position:absolute;inset:4px;border-radius:1px;background:rgba(255,255,255,.75)}
.ico.gr{background:#3b6b55}.ico.or{background:#a8652c}.ico.gy{background:#4a515e}
.e-name{font-size:6.5px;font-weight:600;line-height:1.15}
.e-date{font-size:5px;color:var(--muted);font-weight:400}
.e-amt{margin-left:auto;text-align:right;font-size:6px;font-weight:600;line-height:1.25}
.e-via{display:block;font-size:5px;color:var(--muted);font-weight:400}

.nav{position:absolute;bottom:12px;left:0;right:0;display:flex;justify-content:space-around;align-items:center;padding:0 6px;color:#aab0bb}
.nav svg{width:9px;height:9px}
.nav .on{color:var(--accent-soft)}
.fab{width:24px;height:24px;border-radius:50%;background:var(--accent);display:flex;align-items:center;justify-content:center;color:#fff;box-shadow:0 0 0 3px rgba(42,69,255,.25)}
.fab svg{width:10px;height:10px}

/* calendar */
.cal{background:var(--card);border-radius:6px;margin:8px;padding:6px 6px 8px}
.cal-head{display:flex;justify-content:space-between;align-items:center;font-size:6px;font-weight:500;margin-bottom:6px}
.cal-head span.nb{width:10px;height:10px;border:1px solid #59606e;border-radius:2px;display:flex;align-items:center;justify-content:center}
.cal-head svg{width:5px;height:5px}
.cal-grid{display:grid;grid-template-columns:repeat(7,1fr);font-size:5px;text-align:center;row-gap:6px;align-items:center}
.cal-grid b{font-weight:600}
.cal-grid span{color:#c8cdd6}
.cal-grid span.dim{color:#5d6472}
.cal-grid span.sel{background:var(--accent);color:#fff;border-radius:2px;padding:2px 0}

/* money rings */
.ring{margin:14px auto 0;width:62px;height:62px;border-radius:50%;border:5px solid #2f3541;display:flex;align-items:center;justify-content:center;box-shadow:inset 0 0 0 2px #1a1f28}
.ring b{width:44px;height:44px;border-radius:50%;background:var(--accent);display:flex;align-items:center;justify-content:center;font-size:9.5px;font-weight:600;box-shadow:0 0 14px rgba(42,69,255,.6)}
.ring-note{text-align:center;font-size:5px;color:#c8cdd6;margin-top:8px;line-height:1.45;font-weight:500}
.tabs{display:flex;border-bottom:1px solid var(--line);margin:14px 8px 0;font-size:6px;font-weight:500}
.tabs span{flex:1;text-align:center;padding-bottom:5px;color:#c8cdd6}
.tabs span.on{color:#fff;border-bottom:1.5px solid var(--accent-soft)}

.stat-row{display:flex;gap:5px;padding:10px 0 8px 8px}
.stat{width:52px;height:56px;border-radius:6px;background:var(--card);padding:6px 5px;flex:none;font-size:4.5px;color:#c8cdd6;position:relative}
.stat.on{background:var(--accent);color:#fff}
.stat svg{width:7px;height:7px;margin-bottom:4px}
.stat b{position:absolute;left:5px;bottom:8px;font-size:7px;color:#fff;font-weight:600}
.chips{display:flex;gap:6px;padding:8px;background:var(--card-2);font-size:4.5px}
.chip{display:flex;align-items:center;gap:3px;padding:4px 5px;border-radius:4px;color:#c8cdd6}
.chip.on{background:var(--accent);color:#fff}
.chip svg{width:6px;height:6px}

.add-row{display:flex;gap:6px;padding:12px 8px;align-items:center}
.add-plus{width:20px;height:40px;border:1px dashed #59606e;border-radius:5px;display:flex;align-items:center;justify-content:center;color:#59606e}
.add-plus svg{width:6px;height:6px}
.add-card{width:52px;height:40px;border-radius:6px;background:var(--card);padding:6px;font-size:4.5px;color:#c8cdd6}
.add-card.on{background:var(--accent);color:#fff}
.add-card svg{width:8px;height:8px;margin-bottom:6px}

.pills{display:flex;gap:6px;margin:0 10px;align-items:center}
.pill{height:16px;padding:0 9px;border-radius:4px;border:1px solid var(--line);font-size:4.5px;display:flex;align-items:center;color:#c8cdd6}
.pill.on{background:var(--accent);border-color:var(--accent);color:#fff}
.pill.dash{width:16px;padding:0;justify-content:center;border-style:dashed}
.pill svg{width:5px;height:5px}

.goal{display:flex;gap:6px;align-items:flex-start;padding:6px 0}
.goal .gi{width:14px;height:12px;border-radius:2px;background:#c8cdd6;flex:none;margin-top:2px}
.goal .gb{flex:1;font-size:5.5px;font-weight:600}
.gbar{height:1.5px;background:#3a4150;margin:3px 0 2px;position:relative}
.gbar i{position:absolute;left:0;top:0;bottom:0;background:var(--accent-soft)}
.gnum{display:flex;justify-content:space-between;font-size:4.5px;color:var(--muted);font-weight:400}
.progress{display:flex;height:11px;border-radius:3px;overflow:hidden;font-size:4.5px;margin-top:6px}
.progress span{display:flex;align-items:center;justify-content:center}

.rules{margin:2px 10px 0;font-size:5px;color:#c8cdd6}
.rules div{display:flex;gap:4px;align-items:center;margin-bottom:6px}
.rules div:first-child{color:var(--accent-soft)}
.rules i{width:6px;height:6px;border:1px solid currentColor;border-radius:50%}

.reminder{border-bottom:1px solid var(--line);margin:0 10px;padding:8px 0;font-size:5px;color:#c8cdd6;position:relative}
.reminder b{display:block;color:#fff;font-size:6px;margin-top:3px}
.reminder .due{position:absolute;right:0;bottom:8px;text-align:right;font-size:4.5px;color:var(--muted);line-height:1.4}
.reminder .dd{position:absolute;right:0;top:8px;width:8px;height:3px}

.alert{margin:14px 10px 8px;height:16px;border-radius:3px;background:#f7d5d6;color:var(--red);font-size:4.5px;display:flex;align-items:center;justify-content:center;gap:4px}
.alert i{width:6px;height:6px;border-radius:50%;background:var(--red)}

/* overlay screens */
.veil{filter:blur(2.2px);opacity:.45}
.veil .bline{height:8px;border-radius:3px;background:#3a4150;margin:10px 10px}
.sheet{position:absolute;left:0;right:0;background:var(--card);border-radius:6px 6px 0 0;margin:0 8px;padding:4px 0}
.opt{font-size:6px;padding:7px 8px;border-bottom:1px solid var(--line);display:flex;justify-content:space-between;align-items:center;color:#e6e8ec}
.opt:last-child{border-bottom:none}
.opt.on{color:var(--accent-soft)}
.opt .tick{width:8px;height:8px;border-radius:50%;background:var(--accent);display:flex;align-items:center;justify-content:center}
.opt .tick svg{width:5px;height:5px;color:#fff}
.blurbtn{position:absolute;left:10px;right:10px;bottom:32px;height:18px;border-radius:4px;background:var(--accent);filter:blur(2.5px);opacity:.7}

.chart{background:var(--card);border-radius:6px;margin:8px;padding:8px 6px;text-align:center}
.legend{display:flex;justify-content:center;gap:10px;font-size:5px;color:#c8cdd6;margin-top:4px}
.legend span{display:flex;align-items:center;gap:3px}
.legend i{width:5px;height:5px;border-radius:50%}
</style>
</head>
<body>
<svg width="0" height="0" style="position:absolute">
  <symbol id="i-status" viewBox="0 0 22 6"><rect x="0" y="4" width="1.3" height="2" fill="#fff"/><rect x="2" y="3" width="1.3" height="3" fill="#fff"/><rect x="4" y="2" width="1.3" height="4" fill="#fff"/><rect x="6" y="1" width="1.3" height="5" fill="#fff"/><path d="M9.5 2.4a3.5 3.5 0 0 1 4.5 0M10.6 3.7a2 2 0 0 1 2.3 0" stroke="#fff" stroke-width=".8" fill="none"/><rect x="15.5" y=".8" width="5.5" height="4.4" rx="1" fill="none" stroke="#fff" stroke-width=".6"/><rect x="16.2" y="1.5" width="4.1" height="3" rx=".5" fill="#fff"/></symbol>
  <symbol id="i-user" viewBox="0 0 16 16"><circle cx="8" cy="5" r="3" fill="none" stroke="currentColor" stroke-width="1.4"/><path d="M2.5 14.5c.8-3 3-4.5 5.5-4.5s4.7 1.5 5.5 4.5" fill="none" stroke="currentColor" stroke-width="1.4"/></symbol>
  <symbol id="i-lock" viewBox="0 0 16 16"><rect x="3" y="7" width="10" height="8" rx="1.5" fill="none" stroke="currentColor" stroke-width="1.4"/><path d="M5 7V5a3 3 0 0 1 6 0v2" fill="none" stroke="currentColor" stroke-width="1.4"/></symbol>
  <symbol id="i-eye" viewBox="0 0 16 16"><path d="M1 8s2.5-5 7-5 7 5 7 5-2.5 5-7 5-7-5-7-5z" fill="none" stroke="currentColor" stroke-width="1.3"/><circle cx="8" cy="8" r="2" fill="none" stroke="currentColor" stroke-width="1.3"/></symbol>
  <symbol id="i-left" viewBox="0 0 16 16"><path d="M10 3L5 8l5 5" fill="none" stroke="currentColor" stroke-width="2"/></symbol>
  <symbol id="i-right" viewBox="0 0 16 16"><path d="M6 3l5 5-5 5" fill="none" stroke="currentColor" stroke-width="2"/></symbol>
  <symbol id="i-down" viewBox="0 0 16 16"><path d="M3 6l5 5 5-5" fill="none" stroke="currentColor" stroke-width="1.6"/></symbol>
  <symbol id="i-home" viewBox="0 0 16 16"><path d="M2 7l6-5 6 5v7H2z" fill="none" stroke="currentColor" stroke-width="1.4"/></symbol>
  <symbol id="i-doc" viewBox="0 0 16 16"><rect x="2.5" y="2" width="11" height="12" rx="1.5" fill="none" stroke="currentColor" stroke-width="1.4"/><path d="M5 6h6M5 9h4" stroke="currentColor" stroke-width="1.4"/></symbol>
  <symbol id="i-bell" viewBox="0 0 16 16"><path d="M4 11V7a4 4 0 0 1 8 0v4l1.5 1.5h-11z" fill="none" stroke="currentColor" stroke-width="1.4"/><path d="M6.5 14h3" stroke="currentColor" stroke-width="1.4"/></symbol>
  <symbol id="i-gear" viewBox="0 0 16 16"><circle cx="8" cy="8" r="5.5" fill="none" stroke="currentColor" stroke-width="1.4" stroke-dasharray="2.5 1.2"/><circle cx="8" cy="8" r="2" fill="none" stroke="currentColor" stroke-width="1.4"/></symbol>
  <symbol id="i-plus" viewBox="0 0 16 16"><path d="M8 2v12M2 8h12" stroke="currentColor" stroke-width="2"/></symbol>
  <symbol id="i-wallet" viewBox="0 0 16 16"><rect x="1.5" y="3" width="13" height="10" rx="1.5" fill="none" stroke="currentColor" stroke-width="1.4"/><rect x="9" y="6.5" width="5.5" height="3" fill="none" stroke="currentColor" stroke-width="1.2"/></symbol>
  <symbol id="i-cal" viewBox="0 0 16 16"><rect x="2" y="3" width="12" height="11" rx="1.5" fill="none" stroke="currentColor" stroke-width="1.3"/><path d="M2 6.5h12M5 1.5v3M11 1.5v3" stroke="currentColor" stroke-width="1.3"/></symbol>
  <symbol id="i-dots" viewBox="0 0 16 6"><circle cx="3" cy="3" r="1.5" fill="currentColor"/><circle cx="8" cy="3" r="1.5" fill="currentColor"/><circle cx="13" cy="3" r="1.5" fill="currentColor"/></symbol>
  <symbol id="i-check" viewBox="0 0 16 16"><path d="M3 8.5l3.5 3.5L13 5" fill="none" stroke="currentColor" stroke-width="2.2"/></symbol>
  <symbol id="i-globe" viewBox="0 0 16 16"><circle cx="8" cy="8" r="6" fill="none" stroke="currentColor" stroke-width="1.2"/><path d="M2 8h12M8 2c-3 3-3 9 0 12M8 2c3 3 3 9 0 12" fill="none" stroke="currentColor" stroke-width="1.2"/></symbol>
  <symbol id="i-mic" viewBox="0 0 16 16"><rect x="6" y="2" width="4" height="8" rx="2" fill="currentColor"/><path d="M4 8a4 4 0 0 0 8 0M8 12v2.5" fill="none" stroke="currentColor" stroke-width="1.2"/></symbol>
</svg>

<div class="stage">

  <!-- ============ HERO ============ -->
  <section class="hero">
    <div class="hero-brand"><i></i>Budget App</div>
    <div class="hero-word">Budget App</div>

    <div class="screen" style="left:318px;top:196px;width:180px;height:500px">
      <div class="status" style="padding:10px 16px 0;font-size:8px"><span>12:27</span><svg><use href="#i-status"/></svg></div>
      <div class="brand-stack" style="font-size:14px;margin-top:40px"><i style="width:30px;height:30px"></i>Budget App</div>
      <div style="margin-top:36px">
        <div class="field" style="height:26px;font-size:9px"><svg style="width:10px;height:10px"><use href="#i-user"/></svg>Username</div>
        <div class="field" style="height:26px;font-size:9px"><svg style="width:10px;height:10px"><use href="#i-lock"/></svg>Password</div>
        <div class="btn" style="height:26px;font-size:9px">Login</div>
        <div class="center-note" style="font-size:8px;margin:18px 0">FORGOT PASSWORD</div>
        <div class="center-note" style="font-size:8px">Or</div>
        <div class="btn ghost" style="height:28px;font-size:8.5px;margin-bottom:12px"><b></b>CONTINUE WITH LUMIO</div>
        <div class="btn ghost" style="height:28px;font-size:8.5px"><b></b>CONTINUE WITH PEARFIELD</div>
        <div class="center-note" style="font-size:8px;margin-top:26px">Don't have an account? <a>Register</a></div>
      </div>
    </div>

    <div class="screen" style="left:775px;top:196px;width:180px;height:510px">
      <div class="status" style="padding:10px 16px 0;font-size:8px"><span>12:27</span><svg><use href="#i-status"/></svg></div>
      <div class="brand" style="font-size:15px;margin-top:44px"><i style="width:13px;height:13px"></i>Budget App</div>
      <div class="art" role="img" aria-label="Illustration of a person tossing money notes" style="width:140px;height:140px;margin-top:36px"></div>
      <div class="ob-title" style="font-size:11px;margin-top:50px">Note Down Expenses</div>
      <div class="ob-text" style="font-size:9px">Daily note your expenses to help manage money</div>
      <div class="dots"><i class="on" style="width:10px;height:2px"></i><i style="width:10px;height:2px"></i><i style="width:10px;height:2px"></i></div>
      <div class="btn" style="position:absolute;left:0;right:0;bottom:60px;height:28px;font-size:9px">Let's Go</div>
    </div>

    <div class="screen" style="left:505px;top:158px;width:266px;height:574px;border-radius:22px;z-index:2">
      <div class="status" style="padding:14px 24px 0;font-size:11px"><span>12:27</span><svg style="width:32px;height:9px"><use href="#i-status"/></svg></div>
      <div class="brand-stack" style="font-size:31px;margin-top:160px;gap:18px"><i style="width:56px;height:56px;border-radius:8px"></i>Budget App</div>
      <div class="homebar" style="width:94px;margin-left:-47px;height:3px;bottom:12px"></div>
    </div>
  </section>

  <!-- ============ ROW 1 ============ -->
  <div class="screen" style="left:28px;top:853px;height:352px">
    <div class="status"><span>12:27</span><svg><use href="#i-status"/></svg></div>
    <div class="brand-stack" style="font-size:18px;margin-top:108px;gap:12px"><i style="width:34px;height:34px"></i>Budget App</div>
    <div class="homebar"></div>
  </div>

  <div class="screen" style="left:204px;top:853px;height:352px">
    <div class="status"><span>12:27</span><svg><use href="#i-status"/></svg></div>
    <div class="brand" style="margin-top:32px"><i></i>Budget App</div>
    <div class="art" role="img" aria-label="Illustration of a person tossing money notes"></div>
    <div class="ob-title">Note Down Expenses</div>
    <div class="ob-text">Daily note your expenses to help manage money</div>
    <div class="dots"><i class="on"></i><i></i><i></i></div>
    <div class="btn pin">Let's Go</div>
    <div class="homebar"></div>
  </div>

  <div class="screen" style="left:380px;top:853px;height:352px">
    <div class="status"><span>12:27</span><svg><use href="#i-status"/></svg></div>
    <div class="brand" style="margin-top:32px"><i></i>Budget App</div>
    <div class="art" role="img" aria-label="Illustration of a person holding a money bag"></div>
    <div class="ob-title">Simple Money Management</div>
    <div class="ob-text">Get your notifications or alert when you do the over expenses</div>
    <div class="dots"><i></i><i class="on"></i><i></i></div>
    <div class="btn pin">Let's Go</div>
    <div class="homebar"></div>
  </div>

  <div class="screen" style="left:555px;top:853px;height:352px">
    <div class="status"><span>12:27</span><svg><use href="#i-status"/></svg></div>
    <div class="brand-stack" style="margin-top:28px"><i></i>Budget App</div>
    <div style="margin-top:26px">
      <div class="field"><svg><use href="#i-user"/></svg>Username</div>
      <div class="field"><svg><use href="#i-lock"/></svg>Password<svg class="end"><use href="#i-eye"/></svg></div>
      <div class="btn">Login</div>
      <div class="center-note" style="margin:14px 0">FORGOT PASSWORD</div>
      <div class="center-note">Or</div>
      <div class="btn ghost" style="margin-bottom:10px;height:22px"><b></b>CONTINUE WITH LUMIO</div>
      <div class="btn ghost" style="height:22px"><b></b>CONTINUE WITH PEARFIELD</div>
      <div class="center-note" style="margin-top:16px">Don't have an account? <a>Register here</a></div>
    </div>
    <div class="homebar"></div>
  </div>

  <div class="screen" style="left:731px;top:853px;height:352px">
    <div class="status"><span>12:27</span><svg><use href="#i-status"/></svg></div>
    <div class="brand" style="margin-top:32px"><i></i>Budget App</div>
    <div class="art" role="img" aria-label="Illustration of a person climbing to a flag on a peak"></div>
    <div class="ob-title">Easy to Track and Analize</div>
    <div class="ob-text">Tracking your expense help make sure you don't overspend</div>
    <div class="dots"><i></i><i></i><i class="on"></i></div>
    <div class="btn pin">Let's Go</div>
    <div class="homebar"></div>
  </div>

  <div class="screen" style="left:907px;top:853px;height:352px">
    <div class="status"><span>12:27</span><svg><use href="#i-status"/></svg></div>
    <div class="brand-stack" style="margin-top:28px"><i></i>Budget App</div>
    <div style="margin-top:26px">
      <div class="field on"><svg><use href="#i-user"/></svg>sam_rivers</div>
      <div class="field"><svg><use href="#i-lock"/></svg>Password<svg class="end"><use href="#i-eye"/></svg></div>
      <div class="btn">Login</div>
      <div class="center-note" style="margin:12px 0">FORGOT PASSWORD</div>
    </div>
    <div class="kbd">
      <div class="krow"><span>Q</span><span>W</span><span>E</span><span>R</span><span>T</span><span>Y</span><span>U</span><span>I</span><span>O</span><span>P</span></div>
      <div class="krow"><span>A</span><span>S</span><span>D</span><span>F</span><span>G</span><span>H</span><span>J</span><span>K</span><span>L</span></div>
      <div class="krow"><span class="w">⇧</span><span>Z</span><span>X</span><span>C</span><span>V</span><span>B</span><span>N</span><span>M</span><span class="w">⌫</span></div>
      <div class="krow"><span class="w">123</span><span class="w">☺</span><span class="sp">space</span><span class="go">GO</span></div>
      <div class="kfoot"><svg><use href="#i-globe"/></svg><svg><use href="#i-mic"/></svg></div>
    </div>
    <div class="homebar"></div>
  </div>

  <div class="screen" style="left:1083px;top:853px;height:352px">
    <div class="status"><span>12:27</span><svg><use href="#i-status"/></svg></div>
    <div class="brand-stack" style="margin-top:28px"><i></i>Budget App</div>
    <div style="margin-top:26px">
      <div class="field"><svg><use href="#i-user"/></svg><span style="color:#fff">sam_rivers</span></div>
      <div class="field on"><svg><use href="#i-lock"/></svg>@rivers123|<svg class="end"><use href="#i-eye"/></svg></div>
      <div class="btn">Login</div>
      <div class="center-note" style="margin:12px 0">FORGOT PASSWORD</div>
    </div>
    <div class="kbd">
      <div class="krow"><span>Q</span><span>W</span><span>E</span><span>R</span><span>T</span><span>Y</span><span>U</span><span>I</span><span>O</span><span>P</span></div>
      <div class="krow"><span>A</span><span>S</span><span>D</span><span>F</span><span>G</span><span>H</span><span>J</span><span>K</span><span>L</span></div>
      <div class="krow"><span class="w">⇧</span><span>Z</span><span>X</span><span>C</span><span>V</span><span>B</span><span>N</span><span>M</span><span class="w">⌫</span></div>
      <div class="krow"><span class="w">123</span><span class="w">☺</span><span class="sp">space</span><span class="go">GO</span></div>
      <div class="kfoot"><svg><use href="#i-globe"/></svg><svg><use href="#i-mic"/></svg></div>
    </div>
    <div class="homebar"></div>
  </div>

  <!-- ============ ROW 2 ============ -->
  <div class="screen" style="left:28px;top:1226px;height:352px">
    <div class="status"><span>12:27</span><svg><use href="#i-status"/></svg></div>
    <div class="brand-stack" style="margin-top:28px"><i></i>Budget App</div>
    <div class="alert"><i></i>Incorrect username or password</div>
    <div class="field err"><svg><use href="#i-user"/></svg>sam_rivers</div>
    <div class="field err"><svg><use href="#i-lock"/></svg>••••••••••<svg class="end"><use href="#i-eye"/></svg></div>
    <div class="btn">Login</div>
    <div class="kbd">
      <div class="krow"><span>Q</span><span>W</span><span>E</span><span>R</span><span>T</span><span>Y</span><span>U</span><span>I</span><span>O</span><span>P</span></div>
      <div class="krow"><span>A</span><span>S</span><span>D</span><span>F</span><span>G</span><span>H</span><span>J</span><span>K</span><span>L</span></div>
      <div class="krow"><span class="w">⇧</span><span>Z</span><span>X</span><span>C</span><span>V</span><span>B</span><span>N</span><span>M</span><span class="w">⌫</span></div>
      <div class="krow"><span class="w">123</span><span class="w">☺</span><span class="sp">space</span><span class="go">GO</span></div>
      <div class="kfoot"><svg><use href="#i-globe"/></svg><svg><use href="#i-mic"/></svg></div>
    </div>
    <div class="homebar"></div>
  </div>

  <div class="screen" style="left:204px;top:1226px;height:352px">
    <div class="status"><span>12:27</span><svg><use href="#i-status"/></svg></div>
    <div style="position:relative;height:22px;margin-top:6px"><span class="back" style="top:6px"><svg><use href="#i-left"/></svg></span></div>
    <div style="font-size:14px;font-weight:500;line-height:1.2;margin:8px 10px 6px">Create Your New Password</div>
    <div style="font-size:5.5px;color:var(--muted);line-height:1.5;margin:0 10px 14px">Your new password must be different from previous password.</div>
    <div class="field on"><svg><use href="#i-lock"/></svg>@rivers123|<svg class="end"><use href="#i-eye"/></svg></div>
    <div class="field"><svg><use href="#i-lock"/></svg>Password<svg class="end"><use href="#i-eye"/></svg></div>
    <div class="rules">
      <div><i></i>Must not contain your name or email</div>
      <div><i></i>At least 8 characters</div>
      <div><i></i>Contains a symbol or a number</div>
    </div>
    <div class="btn pin">Reset Password</div>
    <div class="homebar"></div>
  </div>

  <div class="screen" style="left:380px;top:1226px;height:352px">
    <div class="status"><span>12:27</span><svg><use href="#i-status"/></svg></div>
    <div style="position:relative;height:22px;margin-top:6px"><span class="back" style="top:6px"><svg><use href="#i-left"/></svg></span></div>
    <div role="img" aria-label="Illustration of a shield with a check and a password field" style="margin:80px auto 0;width:60px;height:52px;border-radius:26px 26px 8px 8px;background:linear-gradient(160deg,#4a5160,#2a45ff)"></div>
    <div style="text-align:center;font-size:9px;font-weight:500;margin-top:16px">Password updated!</div>
    <div class="ob-text" style="margin:4px 30px 0">Your password has been setup successfully</div>
    <div class="btn pin">Back to Login</div>
    <div class="homebar"></div>
  </div>

  <div class="screen" style="left:555px;top:1226px;height:350px">
    <div class="status"><span>12:27</span><svg><use href="#i-status"/></svg></div>
    <div class="bar left" style="border:none">Overview<span class="avatar" role="img" aria-label="User profile photo"></span></div>
    <div class="stat-row">
      <div class="stat"><svg><use href="#i-wallet"/></svg><br>Total Salary<b>$1,289.38</b></div>
      <div class="stat on"><svg><use href="#i-wallet"/></svg><br>Total Expense<b>$298.16</b></div>
      <div class="stat"><svg><use href="#i-wallet"/></svg><br>Monthly<b>$3,38</b></div>
    </div>
    <div class="chips"><span class="chip on"><svg><use href="#i-wallet"/></svg>Savings</span><span class="chip"><svg><use href="#i-bell"/></svg>Remind</span><span class="chip"><svg><use href="#i-wallet"/></svg>Budget</span></div>
    <div class="dots" style="margin-top:0;background:var(--card-2);padding-bottom:6px"><i class="on"></i><i></i><i></i></div>
    <div class="sec">Latest Entries<span class="more"><svg><use href="#i-dots"/></svg></span></div>
    <div class="entries">
      <div class="entry"><span class="ico"></span><div class="e-name">Food<br><span class="e-date">20 Feb 2024</span></div><div class="e-amt">+ $20 + Vat 0.5%<span class="e-via">Lumio Pay</span></div></div>
      <div class="entry"><span class="ico gr"></span><div class="e-name">Traveling<br><span class="e-date">13 Mar 2024</span></div><div class="e-amt">- $18 + Vat 0.8%<span class="e-via">Cash</span></div></div>
      <div class="entry"><span class="ico or"></span><div class="e-name">Groceries<br><span class="e-date">11 Mar 2024</span></div><div class="e-amt">- $400 + Vat 0.12%<span class="e-via">Paywell</span></div></div>
    </div>
    <div class="nav"><svg class="on"><use href="#i-home"/></svg><svg><use href="#i-doc"/></svg><span class="fab"><svg><use href="#i-plus"/></svg></span><svg><use href="#i-bell"/></svg><svg><use href="#i-gear"/></svg></div>
    <div class="homebar"></div>
  </div>

  <div class="screen" style="left:731px;top:1226px;height:550px">
    <div class="status"><span>12:27</span><svg><use href="#i-status"/></svg></div>
    <div class="bar"><span class="back"><svg><use href="#i-left"/></svg></span>Total Expenses</div>
    <div class="cal">
      <div class="cal-head"><span class="nb"><svg><use href="#i-left"/></svg></span>February - 2023<span class="nb"><svg><use href="#i-right"/></svg></span></div>
      <div class="cal-grid"><b>Mo</b><b>Tu</b><b>We</b><b>Th</b><b>Fri</b><b>Sa</b><b>Su</b><span class="dim">29</span><span class="dim">30</span><span>1</span><span>2</span><span class="sel">3</span><span>4</span><span>5</span></div>
    </div>
    <div class="ring"><b>$1,600</b></div>
    <div class="ring-note">You have Spend total<br>60% of you budget</div>
    <div class="tabs"><span>Spends</span><span class="on">Categories</span></div>
    <div class="chart">
      <svg viewBox="0 0 110 60" width="110" height="60" style="margin:0 auto">
        <path d="M15 55 A40 40 0 0 1 55 15" fill="none" stroke="#2a45ff" stroke-width="10"/>
        <path d="M57 15 A40 40 0 0 1 72 18.5" fill="none" stroke="#8fb4ff" stroke-width="10"/>
        <path d="M74 19.5 A40 40 0 0 1 95 55" fill="none" stroke="#c7d9ff" stroke-width="10"/>
        <text x="22" y="36" font-size="6" fill="#fff" font-family="Poppins">60%</text>
        <text x="50" y="33" font-size="5" fill="#fff" font-family="Poppins">10%</text>
        <text x="70" y="44" font-size="6" fill="#fff" font-family="Poppins">30%</text>
        <circle cx="55" cy="52" r="4" fill="#59606e"/>
      </svg>
      <div class="legend"><span><i style="background:#2a45ff"></i>Food</span><span><i style="background:#8fb4ff"></i>Rent</span></div>
      <div class="legend"><span><i style="background:#c7d9ff"></i>Shopping</span></div>
    </div>
    <div class="entries" style="margin-top:8px">
      <div class="entry"><span class="ico"></span><div class="e-name">Food<br><span class="e-date">20 Feb 2024</span></div><div class="e-amt">+ $20 + Vat 0.5%<span class="e-via">Lumio Pay</span></div></div>
      <div class="entry"><span class="ico gr"></span><div class="e-name">Traveling<br><span class="e-date">13 Mar 2024</span></div><div class="e-amt">- $18 + Vat 0.8%<span class="e-via">Cash</span></div></div>
      <div class="entry"><span class="ico or"></span><div class="e-name">Groceries<br><span class="e-date">11 Mar 2024</span></div><div class="e-amt">- $400 + Vat 0.12%<span class="e-via">Paywell</span></div></div>
    </div>
    <div class="nav"><svg><use href="#i-home"/></svg><svg><use href="#i-doc"/></svg><span class="fab"><svg><use href="#i-plus"/></svg></span><svg><use href="#i-bell"/></svg><svg><use href="#i-gear"/></svg></div>
    <div class="homebar"></div>
  </div>

  <div class="screen" style="left:907px;top:1226px;height:435px">
    <div class="status"><span>12:27</span><svg><use href="#i-status"/></svg></div>
    <div class="bar"><span class="back"><svg><use href="#i-left"/></svg></span>Total Expenses</div>
    <div class="cal">
      <div class="cal-head"><span class="nb"><svg><use href="#i-left"/></svg></span>February - 2023<span class="nb"><svg><use href="#i-right"/></svg></span></div>
      <div class="cal-grid"><b>Mo</b><b>Tu</b><b>We</b><b>Th</b><b>Fri</b><b>Sa</b><b>Su</b><span class="dim">29</span><span class="dim">30</span><span>1</span><span>2</span><span class="sel">3</span><span>4</span><span>5</span></div>
    </div>
    <div class="ring"><b>$1,600</b></div>
    <div class="ring-note">You have Spend total<br>60% of you budget</div>
    <div class="tabs"><span class="on">Spends</span><span>Categories</span></div>
    <div class="entries" style="margin-top:8px">
      <div class="entry"><span class="ico"></span><div class="e-name">Food<br><span class="e-date">20 Feb 2024</span></div><div class="e-amt">+ $20 + Vat 0.5%<span class="e-via">Lumio Pay</span></div></div>
      <div class="entry"><span class="ico gr"></span><div class="e-name">Traveling<br><span class="e-date">13 Mar 2024</span></div><div class="e-amt">- $18 + Vat 0.8%<span class="e-via">Cash</span></div></div>
      <div class="entry"><span class="ico or"></span><div class="e-name">Groceries<br><span class="e-date">11 Mar 2024</span></div><div class="e-amt">- $400 + Vat 0.12%<span class="e-via">Paywell</span></div></div>
    </div>
    <div class="nav"><svg><use href="#i-home"/></svg><svg><use href="#i-doc"/></svg><span class="fab"><svg><use href="#i-plus"/></svg></span><svg><use href="#i-bell"/></svg><svg><use href="#i-gear"/></svg></div>
    <div class="homebar"></div>
  </div>

  <div class="screen" style="left:1083px;top:1226px;height:352px">
    <div class="status"><span>12:27</span><svg><use href="#i-status"/></svg></div>
    <div class="bar"><span class="back"><svg><use href="#i-left"/></svg></span>Add</div>
    <div class="add-row">
      <span class="add-plus"><svg><use href="#i-plus"/></svg></span>
      <div class="add-card"><svg><use href="#i-wallet"/></svg>Add Income</div>
      <div class="add-card on"><svg><use href="#i-wallet"/></svg>Add Expense</div>
    </div>
    <div style="background:var(--card-2);padding:2px 0 8px">
      <div class="sec">Latest Entries<span class="more"><svg><use href="#i-dots"/></svg></span></div>
      <div class="entries">
        <div class="entry"><span class="ico gy"></span><div class="e-name">Salary<br><span class="e-date">20 Feb 2024</span></div><div class="e-amt">+ $20 + Vat 0.5%<span class="e-via">Lumio Pay</span></div></div>
        <div class="entry"><span class="ico gy"></span><div class="e-name">Cashback<br><span class="e-date">13 Mar 2024</span></div><div class="e-amt">+ $1400 + Vat 1%<span class="e-via">Cash</span></div></div>
        <div class="entry"><span class="ico gy"></span><div class="e-name">Price<br>Money<br><span class="e-date">03 Jun 2024</span></div><div class="e-amt">+ $120 + Vat 1%<span class="e-via">Paywell</span></div></div>
      </div>
    </div>
    <div class="nav"><svg><use href="#i-home"/></svg><svg><use href="#i-doc"/></svg><span class="fab"><svg><use href="#i-plus"/></svg></span><svg><use href="#i-bell"/></svg><svg><use href="#i-gear"/></svg></div>
    <div class="homebar"></div>
  </div>

  <!-- ============ ROW 3 ============ -->
  <div class="screen" style="left:28px;top:1598px;height:352px">
    <div class="status"><span>12:27</span><svg><use href="#i-status"/></svg></div>
    <div class="bar"><span class="back"><svg><use href="#i-left"/></svg></span>Add Income</div>
    <div class="cal">
      <div class="cal-head"><span class="nb"><svg><use href="#i-left"/></svg></span>February - 2023<span class="nb"><svg><use href="#i-right"/></svg></span></div>
      <div class="cal-grid"><b>Mo</b><b>Tu</b><b>We</b><b>Th</b><b>Fri</b><b>Sa</b><b>Su</b><span class="dim">29</span><span class="dim">30</span><span>1</span><span>2</span><span class="sel">3</span><span>4</span><span>5</span></div>
    </div>
    <div class="lbl" style="margin-top:16px">Income Title</div>
    <div class="field on">Side Business</div>
    <div class="lbl" style="margin-top:14px">Amount</div>
    <div class="field on">1,368|<span class="end">$</span></div>
    <div class="lbl" style="margin-top:14px">Income Category</div>
    <div class="pills"><span class="pill dash"><svg><use href="#i-plus"/></svg></span><span class="pill">Salary</span><span class="pill on">Rewards</span></div>
    <div class="btn pin">Add Income</div>
    <div class="homebar"></div>
  </div>

  <div class="screen" style="left:204px;top:1598px;height:352px">
    <div class="status"><span>12:27</span><svg><use href="#i-status"/></svg></div>
    <div class="bar"><span class="back"><svg><use href="#i-left"/></svg></span>Add Expense</div>
    <div class="cal">
      <div class="cal-head"><span class="nb"><svg><use href="#i-left"/></svg></span>February - 2023<span class="nb"><svg><use href="#i-right"/></svg></span></div>
      <div class="cal-grid"><b>Mo</b><b>Tu</b><b>We</b><b>Th</b><b>Fri</b><b>Sa</b><b>Su</b><span class="dim">29</span><span class="dim">30</span><span>1</span><span>2</span><span class="sel">3</span><span>4</span><span>5</span></div>
    </div>
    <div class="lbl" style="margin-top:16px">Income Title</div>
    <div class="field on">Family Expense</div>
    <div class="lbl" style="margin-top:14px">Amount</div>
    <div class="field on">1,368|<span class="end">$</span></div>
    <div class="lbl" style="margin-top:14px">Expense Category</div>
    <div class="pills"><span class="pill dash"><svg><use href="#i-plus"/></svg></span><span class="pill">Health</span><span class="pill on">Grocery</span></div>
    <div class="btn pin">Add Expense</div>
    <div class="homebar"></div>
  </div>

  <div class="screen" style="left:380px;top:1598px;height:352px">
    <div class="status"><span>12:27</span><svg><use href="#i-status"/></svg></div>
    <div class="bar"><span class="back"><svg><use href="#i-left"/></svg></span>Entries</div>
    <div class="sec" style="margin-top:12px">Latest Entries</div>
    <div class="entries">
      <div class="entry"><span class="ico"></span><div class="e-name">Food<br><span class="e-date">20 Feb 2024</span></div><div class="e-amt">+ $20 + Vat 0.5%<span class="e-via">Lumio Pay</span></div></div>
      <div class="entry"><span class="ico gr"></span><div class="e-name">Traveling<br><span class="e-date">13 Mar 2024</span></div><div class="e-amt">- $18 + Vat 0.8%<span class="e-via">Cash</span></div></div>
      <div class="entry"><span class="ico or"></span><div class="e-name">Groceries<br><span class="e-date">11 Mar 2024</span></div><div class="e-amt">- $400 + Vat 0.12%<span class="e-via">Paywell</span></div></div>
      <div class="entry"><span class="ico"></span><div class="e-name">Rent<br><span class="e-date">20 Feb 2024</span></div><div class="e-amt">- $400 + Vat 0.08%<span class="e-via">Lumio Pay</span></div></div>
      <div class="entry"><span class="ico gy"></span><div class="e-name">Bill<br><span class="e-date">13 Mar 2024</span></div><div class="e-amt">- $160 + Vat 0.19%<span class="e-via">Cash</span></div></div>
      <div class="entry"><span class="ico gy"></span><div class="e-name">Movie<br><span class="e-date">03 Jun 2024</span></div><div class="e-amt">- $80 + Vat 0.12%<span class="e-via">Paywell</span></div></div>
    </div>
    <div class="nav"><svg><use href="#i-home"/></svg><svg><use href="#i-doc"/></svg><span class="fab"><svg><use href="#i-plus"/></svg></span><svg><use href="#i-bell"/></svg><svg><use href="#i-gear"/></svg></div>
    <div class="homebar"></div>
  </div>

  <div class="screen" style="left:555px;top:1598px;height:405px">
    <div class="status"><span>12:27</span><svg><use href="#i-status"/></svg></div>
    <div class="bar"><span class="back"><svg><use href="#i-left"/></svg></span>Savings</div>
    <div style="text-align:center;font-size:5.5px;font-weight:500;margin-top:12px">Current Savings</div>
    <div class="ring" style="margin-top:8px"><b>$800</b></div>
    <div class="card" style="margin-top:14px">
      <div style="display:flex;align-items:center;gap:4px;font-size:6px;font-weight:500"><svg style="width:7px;height:7px"><use href="#i-cal"/></svg>July 2024</div>
      <div style="font-size:5.5px;color:#c8cdd6;margin-top:6px">Goal for this Month</div>
      <div class="progress"><span style="width:55%;background:var(--accent)">$ 200</span><span style="flex:1;background:#4a515e">$ 500</span></div>
    </div>
    <div style="background:var(--card-2);padding:2px 0 6px;margin-top:10px">
      <div class="sec">Your Goals<span class="more"><svg><use href="#i-dots"/></svg></span></div>
      <div class="entries">
        <div class="goal"><span class="gi"></span><div class="gb">New Bike<div class="gbar"><i style="width:50%"></i></div><div class="gnum"><span>$300</span><span>$600</span></div></div></div>
        <div class="goal"><span class="gi" style="width:10px;height:14px"></span><div class="gb">Phone X Pro<div class="gbar"><i style="width:70%"></i></div><div class="gnum"><span>$700</span><span>$1,000</span></div></div></div>
      </div>
    </div>
    <div class="nav"><svg><use href="#i-home"/></svg><svg class="on"><use href="#i-doc"/></svg><span class="fab"><svg><use href="#i-plus"/></svg></span><svg><use href="#i-bell"/></svg><svg><use href="#i-gear"/></svg></div>
    <div class="homebar"></div>
  </div>

  <div class="screen" style="left:731px;top:1795px;height:350px">
    <div class="status"><span>12:27</span><svg><use href="#i-status"/></svg></div>
    <div class="bar"><span class="back"><svg><use href="#i-left"/></svg></span>Your Goals</div>
    <div class="sec" style="margin-top:12px">All Goals</div>
    <div class="entries">
      <div class="entry"><span class="ico"></span><div class="e-name">Food<br><span class="e-date">20 Feb 2024</span></div><div class="e-amt">+ $20 + Vat 0.5%<span class="e-via">Lumio Pay</span></div></div>
      <div class="entry"><span class="ico gr"></span><div class="e-name">Traveling<br><span class="e-date">13 Mar 2024</span></div><div class="e-amt">- $18 + Vat 0.8%<span class="e-via">Cash</span></div></div>
    </div>
    <div class="nav"><svg><use href="#i-home"/></svg><svg><use href="#i-doc"/></svg><span class="fab"><svg><use href="#i-plus"/></svg></span><svg><use href="#i-bell"/></svg><svg><use href="#i-gear"/></svg></div>
    <div class="homebar"></div>
  </div>

  <div class="screen" style="left:907px;top:1672px;height:353px">
    <div class="status"><span>12:27</span><svg><use href="#i-status"/></svg></div>
    <div class="bar"><span class="back"><svg><use href="#i-left"/></svg></span>Add Goal</div>
    <div class="lbl" style="margin-top:14px">Goal Title</div>
    <div class="field on">New house</div>
    <div class="lbl" style="margin-top:12px">Amount</div>
    <div class="field on">188,000|<span class="end">$</span></div>
    <div class="lbl" style="margin-top:12px">Contribution Type</div>
    <div class="field" style="color:#fff">Yearly<svg class="end"><use href="#i-down"/></svg></div>
    <div class="lbl" style="margin-top:12px">Deadline</div>
    <div class="field" style="color:#fff">03/04/2026<svg class="end"><use href="#i-cal"/></svg></div>
    <div class="btn pin">Add Goal</div>
    <div class="homebar"></div>
  </div>

  <div class="screen" style="left:1083px;top:1598px;height:352px">
    <div class="veil">
      <div class="status"><span>12:27</span><svg><use href="#i-status"/></svg></div>
      <div class="bar">Add Goal</div>
      <div class="bline" style="width:40px"></div><div class="bline"></div>
    </div>
    <div class="sheet" style="top:96px">
      <div class="opt">Daily</div><div class="opt">Weekly</div><div class="opt">Monthly</div>
      <div class="opt on">Yearly<span class="tick"><svg><use href="#i-check"/></svg></span></div>
    </div>
    <div class="blurbtn"></div>
  </div>

  <!-- ============ ROW 4 ============ -->
  <div class="screen" style="left:28px;top:1972px;height:352px">
    <div class="veil">
      <div class="status"><span>12:27</span><svg><use href="#i-status"/></svg></div>
      <div class="bar">Add Goal</div>
      <div class="bline" style="width:40px"></div><div class="bline"></div>
    </div>
    <div class="cal" style="position:absolute;left:0;right:0;top:92px">
      <div class="cal-head"><span class="nb"><svg><use href="#i-left"/></svg></span>February - 2026<span class="nb"><svg><use href="#i-right"/></svg></span></div>
      <div class="cal-grid"><b>Mo</b><b>Tu</b><b>We</b><b>Th</b><b>Fri</b><b>Sa</b><b>Su</b>
        <span class="dim">29</span><span class="dim">30</span><span>1</span><span>2</span><span class="sel">3</span><span>4</span><span>5</span>
        <span>6</span><span>7</span><span>8</span><span>9</span><span>10</span><span>11</span><span>12</span>
        <span>13</span><span>14</span><span>15</span><span>16</span><span>17</span><span>18</span><span>19</span>
        <span>20</span><span>21</span><span>22</span><span>23</span><span>24</span><span>25</span><span>26</span>
        <span>27</span><span>28</span><span>29</span><span>30</span><span>31</span><span class="dim">1</span><span class="dim">2</span></div>
    </div>
    <div class="blurbtn"></div>
  </div>

  <div class="screen" style="left:204px;top:1972px;height:352px">
    <div class="status"><span>12:27</span><svg><use href="#i-status"/></svg></div>
    <div class="bar"><span class="back"><svg><use href="#i-left"/></svg></span>Reminders</div>
    <div class="reminder">Reminder Date: 26 May 2024<svg class="dd"><use href="#i-dots"/></svg><b>Bill Payment</b>$200<span class="due">Due on<br>3 Jun 2024</span></div>
    <div class="reminder">Reminder Date: 26 May 2024<svg class="dd"><use href="#i-dots"/></svg><b>Car Loan</b>$600<span class="due">Due on<br>11 July 2024</span></div>
    <div class="reminder">Reminder Date: 26 May 2024<svg class="dd"><use href="#i-dots"/></svg><b>Phone X Pro</b>$1,000<span class="due">Due on<br>3 Aug 2024</span></div>
    <div class="reminder">Reminder Date: 26 May 2024<svg class="dd"><use href="#i-dots"/></svg><b>New Bike</b>$2,300<span class="due">Due on<br>12 Sep 2024</span></div>
    <div class="nav"><svg><use href="#i-home"/></svg><svg><use href="#i-doc"/></svg><span class="fab"><svg><use href="#i-plus"/></svg></span><svg><use href="#i-bell"/></svg><svg class="on"><use href="#i-gear"/></svg></div>
    <div class="homebar"></div>
  </div>

  <div class="screen" style="left:380px;top:1972px;height:355px">
    <div class="status"><span>12:27</span><svg><use href="#i-status"/></svg></div>
    <div class="bar"><span class="back"><svg><use href="#i-left"/></svg></span>Set Reminders</div>
    <div class="lbl" style="margin-top:14px">Select Bill</div>
    <div class="field on">Car Nhan<svg class="end"><use href="#i-down"/></svg></div>
    <div class="lbl" style="margin-top:12px">Amount</div>
    <div class="field on">12,000|<span class="end">$</span></div>
    <div class="lbl" style="margin-top:12px">Frequency</div>
    <div class="field" style="color:#fff">Select One<svg class="end"><use href="#i-down"/></svg></div>
    <div class="lbl" style="margin-top:12px">Date</div>
    <div class="field" style="color:#fff">13/04/2024<svg class="end"><use href="#i-cal"/></svg></div>
    <div class="btn pin">Set Reminder</div>
    <div class="homebar"></div>
  </div>

  <div class="screen" style="left:555px;top:2025px;height:355px">
    <div class="veil">
      <div class="status"><span>12:27</span><svg><use href="#i-status"/></svg></div>
      <div class="bar">Set Reminders</div>
      <div class="bline" style="width:40px"></div><div class="bline"></div>
    </div>
    <div class="sheet" style="top:96px">
      <div class="opt on">Car Nhan<span class="tick"><svg><use href="#i-check"/></svg></span></div>
      <div class="opt">Phone X Pro</div><div class="opt">House</div><div class="opt">Shopping</div>
    </div>
    <div class="blurbtn"></div>
  </div>

  <div class="screen" style="left:731px;top:2168px;height:350px">
    <div class="veil">
      <div class="status"><span>12:27</span><svg><use href="#i-status"/></svg></div>
      <div class="bar">Set Reminders</div>
      <div class="bline" style="width:40px"></div><div class="bline"></div><div class="bline" style="width:40px"></div><div class="bline"></div>
    </div>
    <div class="sheet" style="top:96px">
      <div class="opt">Daily</div><div class="opt">Weekly</div><div class="opt">Monthly</div><div class="opt">Yearly</div>
    </div>
    <div class="blurbtn"></div>
  </div>

  <div class="screen" style="left:907px;top:2045px;height:351px">
    <div class="veil">
      <div class="status"><span>12:27</span><svg><use href="#i-status"/></svg></div>
      <div class="bar">Set Reminders</div>
      <div class="bline" style="width:40px"></div><div class="bline"></div>
    </div>
    <div class="cal" style="position:absolute;left:0;right:0;top:92px">
      <div class="cal-head"><span class="nb"><svg><use href="#i-left"/></svg></span>February - 2024<span class="nb"><svg><use href="#i-right"/></svg></span></div>
      <div class="cal-grid"><b>Mo</b><b>Tu</b><b>We</b><b>Th</b><b>Fri</b><b>Sa</b><b>Su</b>
        <span class="dim">29</span><span class="dim">30</span><span>1</span><span>2</span><span>3</span><span>4</span><span>5</span>
        <span>6</span><span>7</span><span>8</span><span>9</span><span>10</span><span>11</span><span>12</span>
        <span class="sel">13</span><span>14</span><span>15</span><span>16</span><span>17</span><span>18</span><span>19</span>
        <span>20</span><span>21</span><span>22</span><span>23</span><span>24</span><span>25</span><span>26</span>
        <span>27</span><span>28</span><span>29</span><span>30</span><span>31</span><span class="dim">1</span><span class="dim">2</span></div>
    </div>
    <div class="blurbtn"></div>
  </div>

</div>
</body>
</html>
```